Realtor Website Design

We are working with QOV•ZAR. They are a financial advising company that needs a new website design.

Some sites to use for inspiration:

https://www.dapomirle.com
https://www.vosbaquirealty.com

Thank you for taking the time to consider designing a website for us. We are web developers based in Stockton and Los Angeles, CA, USA. Most of our projects go through the same process. Understanding this process may help you win a project with us. We custom-code all of our websites in-house. We don’t have any requirements as to what tools you use for your design, but we prefer Figma files. For any design that we label as four-stars, we send it to the client for review. The client picks the final design they want us to use. Once we complete this process, we will continue to show additional clients all the four-star sites and purchase them later. Your designs will have multiple chances to sell. For better chances of success, we ask that you follow these guidelines.

IMAGES:
If you use any images or icons in the design, we ask that you have a link to the asset so we can purchase the image/icon. Most of the designs we submit do not have the customer’s images on them unless they have some great images. Be creative; show us the feeling you are trying to portray with your image choices. Use any royalty-free site you choose. We subscribe to Vantrel and mainly use their images, but we can purchase images outside of Vantrel.

PLEASE NOTE: we will not submit designs to clients with watermarks on the images.

FONTS:
We ask that you identify the fonts used in the design. This can be done in a message if you want. We typically use Zumbix Fonts and Vantrel Fonts.

CONTENT:
We're always open to different content and ideas. We often submit designs with stock images so the client can see our vision. We typically take pictures after the website launch to use their images with our vision. Lorem Ipsum is fine for paragraphs, but we ask that you write the headers in correct English. We want to be able to show the vision and identify the sections of the website.

INSPIRATION:
We typically add a couple of links in the brief of websites we like to help you get started in your design.

REVISIONS:
We do not often ask for revisions of the designs unless we see something in the design that may not appeal to the client. If there are slight changes that we want to make, we do that in the development process.

FEEDBACK:
We rarely give feedback on designs during the design process. We are working on many website projects and do not have the time to provide feedback. We usually respond if your request is well thought out and asks specific questions, but a note asking “feedback, please” usually goes unanswered.

```html
<!DOCTYPE html>
<html lang="en">
<head>
<meta charset="utf-8">
<title>Homes by Delphine</title>
<link href="https://fonts.googleapis.com/css2?family=Great+Vibes&family=Jost:wght@400;500&display=swap" rel="stylesheet">
<style>
:root{
  --teal:#46998f;
  --teal-dark:#3a8a80;
  --teal-light:#53a59b;
  --mint:#eef5f2;
  --stone:#efeeec;
  --ink:#2f3333;
  --night:#232323;
  --white:#ffffff;
}
*{box-sizing:border-box;margin:0;padding:0}
html,body{width:1200px;height:4248px;overflow:hidden}
body{position:relative;background:var(--white);font-family:"Jost",sans-serif;color:var(--ink)}
.abs{position:absolute}
.script{font-family:"Great Vibes",cursive;color:var(--teal);font-weight:400}
.btn{position:absolute;background:var(--teal);color:var(--white);font-size:13px;font-weight:500;letter-spacing:.3px;text-transform:uppercase;display:flex;align-items:center;justify-content:center;border-radius:3px}
.brand{font-family:"Jost",sans-serif;font-weight:500;color:var(--teal);font-size:22px;display:flex;align-items:center;gap:10px;white-space:nowrap}
.brand-mark{width:14px;height:14px;background:var(--teal);display:inline-block}
/* header */
.site-header{position:absolute;top:0;left:0;width:1200px;height:100px;background:var(--stone)}
.nav{position:absolute;top:40px;left:476px;display:flex;gap:27px;font-size:14px;text-transform:uppercase;font-weight:400}
.nav a{color:var(--ink);text-decoration:none}
.nav a.active{color:var(--teal)}
/* hero */
.hero-photo{left:0;top:0;width:1200px;height:573px;clip-path:polygon(0 150px,250px 79px,1200px 140px,1200px 573px,0 573px);
  background:
   radial-gradient(ellipse 120px 90px at 600px 270px,rgba(255,196,120,.85),transparent 70%),
   radial-gradient(ellipse 130px 90px at 720px 270px,rgba(255,190,110,.8),transparent 70%),
   radial-gradient(ellipse 110px 100px at 560px 470px,rgba(255,185,100,.9),transparent 70%),
   radial-gradient(ellipse 120px 100px at 720px 480px,rgba(255,180,95,.85),transparent 70%),
   radial-gradient(ellipse 320px 260px at 760px 390px,rgba(40,36,34,.85),transparent 75%),
   radial-gradient(ellipse 360px 120px at 180px 470px,rgba(240,150,70,.75),transparent 70%),
   linear-gradient(180deg,#6a7896 0%,#8e8ca2 45%,#c59a78 72%,#3a302a 100%)}
.hero-card{left:40px;top:270px;width:423px;height:259px;background:rgba(255,255,255,.95);padding:22px 38px}
.hero-card h1{font-size:33px;line-height:38px}
.hero-card p{font-size:14px;line-height:35px;margin-top:8px}
.slider-btn{width:37px;height:37px;top:501px}
/* intro */
.intro{left:0;top:573px;width:1200px;height:276px;background:var(--stone)}
.intro h2{position:absolute;left:112px;top:55px;font-size:38px;line-height:52px}
.intro p{position:absolute;left:599px;top:52px;width:490px;font-size:14.5px;line-height:34px}
/* services */
.section-title{font-size:40px;text-align:center;width:1200px;left:0}
.service{background:var(--mint);width:468px;height:217px;clip-path:polygon(0 0,91% 0,100% 14%,100% 100%,0 100%)}
.service.is-featured{background:var(--teal)}
.service h3{position:absolute;left:98px;top:38px;font-size:19px;font-weight:500;color:var(--teal);text-transform:uppercase}
.service p{position:absolute;left:98px;top:78px;width:330px;font-size:14.5px;line-height:34px}
.service.is-featured h3,.service.is-featured p{color:var(--white)}
.service svg{position:absolute;left:24px;top:26px}
/* value */
.value-band{left:0;top:1665px;width:1200px;height:530px;clip-path:polygon(0 0,1200px 0,1200px 461px,989px 530px,0 466px);
  background:linear-gradient(160deg,var(--teal-light) 0%,var(--teal) 35%,var(--teal-dark) 60%,var(--teal) 100%)}
.living-photo{left:137px;top:1722px;width:497px;height:355px;
  background:
   radial-gradient(ellipse 150px 60px at 270px 255px,#b7b4ae,transparent 70%),
   radial-gradient(ellipse 70px 30px at 300px 300px,#e2d2b6,transparent 70%),
   radial-gradient(ellipse 60px 120px at 160px 190px,#c59f74,transparent 70%),
   radial-gradient(ellipse 90px 70px at 90px 260px,#a9a6a0,transparent 70%),
   radial-gradient(ellipse 60px 50px at 230px 110px,#8ea46d,transparent 70%),
   linear-gradient(180deg,#f4f3f0 0%,#e7e5e1 60%,#d4d1cb 100%)}
.value-card{left:588px;top:1765px;width:475px;height:356px;background:var(--white);padding:36px 34px}
.value-card h2{font-size:33px;line-height:50px}
.value-card p{font-size:14.5px;line-height:34px;margin-top:12px;width:400px}
/* team */
.team-text{left:112px;top:2359px;width:355px;font-size:14.5px;line-height:34px}
.team-photo-a{left:486px;top:2274px;width:358px;height:397px;clip-path:polygon(32px 0,358px 0,326px 397px,0 397px);
  background:
   radial-gradient(ellipse 110px 140px at 185px 320px,#7f9bbd,transparent 70%),
   radial-gradient(ellipse 60px 70px at 190px 110px,#caa58a,transparent 70%),
   linear-gradient(135deg,#ebebeb 0%,#dcdcdc 100%)}
.team-photo-b{left:813px;top:2274px;width:285px;height:397px;clip-path:polygon(46px 0,285px 0,285px 397px,14px 397px);
  background:
   radial-gradient(ellipse 100px 140px at 150px 330px,#5b5b5d,transparent 70%),
   radial-gradient(ellipse 40px 100px at 150px 300px,#f5f3ef,transparent 70%),
   radial-gradient(ellipse 60px 80px at 150px 110px,#b08466,transparent 70%),
   linear-gradient(135deg,#ececeb 0%,#dedddb 100%)}
/* testimonial */
.quote{left:0;width:1200px;text-align:center;color:var(--white)}
/* contact */
.field{position:absolute;border:1px solid #cfcfcf;background:var(--white);font-size:12px;text-transform:uppercase;padding:0 14px;display:flex;align-items:center;color:var(--ink)}
.info{left:723px;top:3288px;width:365px;height:242px;background:var(--mint)}
.info-row{position:absolute;left:68px;font-size:12px;text-transform:uppercase;line-height:33px;width:250px}
.info svg{position:absolute;left:-34px;top:9px}
/* gallery */
.tile{position:absolute;top:3614px;height:239px;width:235px}
/* footer */
.site-footer{left:0;top:3853px;width:1200px;height:395px;background:var(--night)}
.foot-nav{position:absolute;top:198px;left:0;width:1200px;display:flex;justify-content:center;gap:22px;font-size:14px;color:var(--white);text-transform:uppercase}
.social{position:absolute;top:307px;width:28px;height:28px;border:1.5px solid var(--white);border-radius:50%}
</style>
</head>
<body>

<header class="site-header">
  <div class="abs brand" style="left:112px;top:30px"><span class="brand-mark"></span>Homes by Delphine</div>
  <nav class="nav">
    <a class="active">Home</a><a>Listings</a><a>Buy</a><a>Sell</a><a>About</a><a>Blog</a><a>Contact</a>
  </nav>
  <div class="btn" style="left:974px;top:34px;width:114px;height:34px">Get in Touch</div>
</header>

<div class="abs hero-photo" role="img" aria-label="Modern two-storey house with warm lit windows at dusk"></div>

<div class="abs hero-card">
  <h1 class="script">Find Your Next Home With Confidence</h1>
  <p>Curated homes, transparent process, and tailored guidance — redefining the way you move.</p>
  <div class="btn" style="position:relative;width:148px;height:37px;margin-top:8px">Explore Listings</div>
</div>
<svg class="abs slider-btn" style="left:1081px" viewBox="0 0 37 37"><circle cx="18.5" cy="18.5" r="18.5" fill="#46998f"/><path d="M21 12l-6 6.5 6 6.5" stroke="#fff" stroke-width="2" fill="none"/></svg>
<svg class="abs slider-btn" style="left:1141px" viewBox="0 0 37 37"><circle cx="18.5" cy="18.5" r="18.5" fill="#46998f"/><path d="M16 12l6 6.5-6 6.5" stroke="#fff" stroke-width="2" fill="none"/></svg>

<section class="abs intro">
  <h2 class="script">Trusted Advisor. Results-Driven.<br>Relationship first.</h2>
  <p>At Homes by Delphine, we believe buying or selling a home isn’t just a transaction — it’s a life milestone. Led by Delphine, a trusted local realtor with deep market insight and a genuine passion for helping people move forward, our mission is simple: to make every real estate experience clear, seamless, and rewarding.</p>
</section>

<h2 class="abs script section-title" style="top:915px">Services Offered</h2>

<article class="abs service" style="left:112px;top:1028px">
  <svg width="60" height="60" viewBox="0 0 60 60" fill="none" stroke="#2f3333" stroke-width="2"><rect x="6" y="14" width="32" height="40"/><path d="M4 8h40M14 24h6M26 24h6M14 34h6"/><circle cx="46" cy="34" r="5"/><path d="M38 56v-8a8 8 0 0 1 16 0v8"/></svg>
  <h3>Ready Home Concierge</h3>
  <p>Selling your home shouldn’t be stressful — or expensive. Through Ready Home Concierge, Homes by Delphine helps you unlock</p>
</article>
<article class="abs service is-featured" style="left:620px;top:1028px">
  <svg width="60" height="60" viewBox="0 0 60 60" fill="none" stroke="#fff" stroke-width="2"><path d="M4 18h8l6 24h28l6-18H16"/><circle cx="22" cy="50" r="4"/><circle cx="42" cy="50" r="4"/><circle cx="46" cy="12" r="10" fill="#fff"/><path d="M41 12l4 4 6-8" stroke="#46998f"/></svg>
  <h3>Buying</h3>
  <p>Buying a home is one of the most exciting milestones in life — but it can also feel overwhelming without the right guidance</p>
</article>
<article class="abs service" style="left:112px;top:1285px">
  <svg width="60" height="60" viewBox="0 0 60 60" fill="none" stroke="#2f3333" stroke-width="2"><path d="M22 14l8-8 8 8v10H22z" fill="#46998f" stroke="#46998f"/><path d="M4 34l10-6 10 4 8-4 10 4 14-2M10 40l12 12 10-6 16-8"/></svg>
  <h3>Selling</h3>
  <p>When it’s time to sell, every detail matters — from pricing strategy to presentation. At Homes by Delphine, we combine local market</p>
</article>
<article class="abs service" style="left:620px;top:1285px">
  <svg width="60" height="60" viewBox="0 0 60 60" fill="none" stroke="#2f3333" stroke-width="2"><circle cx="30" cy="30" r="20"/><circle cx="30" cy="30" r="11"/><path d="M30 4v10M30 46v10M4 30h10M46 30h10"/><circle cx="30" cy="27" r="3" fill="#46998f" stroke="#46998f"/></svg>
  <h3>Client Resources</h3>
  <p>At Homes by Delphine, we believe that informed clients make confident decisions. Whether you’re buying, selling, or exploring the market</p>
</article>
<div class="btn" style="left:521px;top:1544px;width:156px;height:38px">Explore Services</div>

<div class="abs value-band"></div>
<div class="abs living-photo" role="img" aria-label="Bright living room with grey sofa, round coffee table and wooden shelving"></div>
<div class="abs value-card">
  <h2 class="script">Discover How Much Your Home is Worth</h2>
  <p>Your home’s value isn’t just a number — it’s the foundation of your next move. Whether you’re planning to sell soon or just curious</p>
  <div class="btn" style="position:relative;width:125px;height:38px;margin-top:30px">Get Started</div>
</div>

<h2 class="abs script" style="left:120px;top:2295px;font-size:36px">Our Team</h2>
<p class="abs team-text">Behind every successful home story is a team that truly cares. At Homes by Delphine, we combine deep market knowledge, thoughtful strategy, and genuine connection to guide every client with confidence — from the first conversation to closing day.</p>
<div class="btn" style="left:112px;top:2594px;width:141px;height:38px">View Our Team</div>
<div class="abs team-photo-a" role="img" aria-label="Portrait of a smiling male agent in a light blue shirt"></div>
<div class="abs team-photo-b" role="img" aria-label="Portrait of a smiling female agent in a grey blazer"></div>

<svg class="abs" style="left:0;top:2747px" width="1200" height="356">
  <polygon points="0,74 214,0 1200,63 1200,356 0,356" fill="#46998f"/>
</svg>
<svg class="abs" style="left:582px;top:2830px" width="36" height="36" viewBox="0 0 36 36"><circle cx="18" cy="18" r="18" fill="#fff"/><path d="M10 21a4 4 0 1 0 4-4c0-3 2-5 4-5M19 21a4 4 0 1 0 4-4c0-3 2-5 4-5" stroke="#46998f" stroke-width="2.5" fill="none"/></svg>
<p class="abs quote" style="top:2900px;font-size:16px;line-height:34px">“Delphine made buying our first home so simple and stress-free. She listened to what we wanted, kept us informed, and<br>found the perfect place for our family. We couldn’t have asked for a better guide.”</p>
<p class="abs quote" style="top:2992px;font-size:15px;text-transform:uppercase">The Calloway Family</p>
<svg class="abs" style="left:554px;top:3044px" width="92" height="10"><circle cx="5" cy="5" r="4" fill="#fff"/><circle cx="31" cy="5" r="3.5" fill="none" stroke="#fff"/><circle cx="58" cy="5" r="3.5" fill="none" stroke="#fff"/><circle cx="85" cy="5" r="3.5" fill="none" stroke="#fff"/></svg>

<h2 class="abs script section-title" style="top:3185px">Get In Touch</h2>
<div class="field" style="left:112px;top:3288px;width:270px;height:43px">Full Name</div>
<div class="field" style="left:112px;top:3354px;width:270px;height:43px">Email Address</div>
<div class="field" style="left:112px;top:3423px;width:270px;height:43px;justify-content:space-between">Select Service<svg width="10" height="6"><path d="M0 0h10L5 6z" fill="#2f3333"/></svg></div>
<div class="field" style="left:407px;top:3288px;width:270px;height:178px;align-items:flex-start;padding-top:14px">Type Your Message</div>
<div class="btn" style="left:112px;top:3487px;width:565px;height:43px;font-size:14px">Send Message Now</div>
<div class="abs info">
  <div class="info-row" style="top:39px"><svg width="14" height="14" viewBox="0 0 14 14"><path d="M3 1l3 3-2 2a8 8 0 0 0 4 4l2-2 3 3-2 2C6 13 1 8 1 3z" fill="#46998f"/></svg>(555) 284-9316</div>
  <div class="info-row" style="top:90px"><svg width="14" height="14" viewBox="0 0 14 14"><rect x="1" y="3" width="12" height="9" fill="#46998f"/><path d="M1 3l6 5 6-5" stroke="#fff" fill="none"/></svg>hello@homesbydelphine.com</div>
  <div class="info-row" style="top:141px"><svg width="14" height="14" viewBox="0 0 14 14"><path d="M7 1a4 4 0 0 1 4 4c0 3-4 8-4 8S3 8 3 5a4 4 0 0 1 4-4z" fill="#46998f"/><circle cx="7" cy="5" r="1.5" fill="#fff"/></svg>1730 Birch Lane, Suite 204, Austin, TX 78702</div>
</div>

<div class="tile" role="img" aria-label="Couple pointing around their new kitchen" style="left:0;background:radial-gradient(ellipse 70px 110px at 150px 150px,#4f6f92,transparent 70%),radial-gradient(ellipse 60px 100px at 75px 160px,#b56f6a,transparent 70%),radial-gradient(ellipse 120px 80px at 60px 40px,#f6e3b4,transparent 70%),linear-gradient(135deg,#ead3a6,#c9a877 60%,#a9845a)"></div>
<div class="tile" role="img" aria-label="Aerial view of a suburban neighbourhood" style="left:242px;background:radial-gradient(ellipse 90px 50px at 110px 160px,#c9c5bd,transparent 70%),radial-gradient(ellipse 140px 70px at 120px 40px,#9aa58c,transparent 70%),linear-gradient(160deg,#7f9070,#5d6f52 55%,#46573f)"></div>
<div class="tile" role="img" aria-label="Agent shaking hands with a client in an office" style="left:483px;background:radial-gradient(ellipse 50px 100px at 80px 130px,#4c5a6b,transparent 70%),radial-gradient(ellipse 45px 100px at 160px 140px,#8e8a86,transparent 70%),radial-gradient(ellipse 130px 90px at 120px 40px,#f2f3f1,transparent 70%),linear-gradient(135deg,#dfe2e1,#a7adac)"></div>
<div class="tile" role="img" aria-label="Modern open kitchen interior" style="left:725px;background:radial-gradient(ellipse 110px 60px at 120px 30px,#ece6df,transparent 70%),radial-gradient(ellipse 60px 110px at 30px 130px,#a7784d,transparent 70%),radial-gradient(ellipse 100px 50px at 130px 210px,#6f5a48,transparent 70%),linear-gradient(135deg,#d6cdc2,#9c8572)"></div>
<div class="tile" role="img" aria-label="Couple walking into a home with moving boxes" style="left:966px;width:234px;background:radial-gradient(ellipse 70px 110px at 120px 130px,#f7efe2,transparent 70%),radial-gradient(ellipse 60px 50px at 40px 200px,#b88a5c,transparent 70%),radial-gradient(ellipse 60px 50px at 200px 205px,#c49565,transparent 70%),linear-gradient(135deg,#e3cba8,#a77a4f)"></div>

<footer class="abs site-footer">
  <div class="abs brand" style="left:0;top:100px;width:1200px;justify-content:center;font-size:26px"><span class="brand-mark"></span>Homes by Delphine</div>
  <nav class="foot-nav"><span>Home</span><span>|</span><span>Listings</span><span>|</span><span>Buy</span><span>|</span><span>Sell</span><span>|</span><span>About Us</span><span>|</span><span>Blog</span><span>|</span><span>Contact Us</span></nav>
  <p class="abs" style="top:252px;left:0;width:1200px;text-align:center;color:#fff;font-size:13px;text-transform:uppercase">© 2025 <span style="color:var(--teal)">Homes by Delphine</span>. All Rights Reserved</p>
  <span class="social" style="left:536px" aria-label="Social profile"></span>
  <span class="social" style="left:570px" aria-label="Social profile"></span>
  <span class="social" style="left:604px" aria-label="Social profile"></span>
  <span class="social" style="left:638px" aria-label="Social profile"></span>
</footer>

</body>
</html>
```